New Business Card Design Project

Need a design that will create an impact / strong impression towards our clients for our business. We are in the lighting business and we do lighting retrofits for large commercial to industrial clientele.

Target Market(s)

Lighting Industry

Industry/Entity Type

Business

Other font styles liked:
• we would like to use the font on our logo, not sure what it is though..

Requirements
Must have
• Our logo.
Nice to have
• We are open to suggestions that have to do with lighting.

```html
<!DOCTYPE html>
<html lang="en">
<head>
<meta charset="utf-8">
<title>Brightline Retrofit Group – Business Card</title>
<link href="https://fonts.googleapis.com/css2?family=Roboto:wght@400;500;700&display=swap" rel="stylesheet">
<style>
  :root {
    --page-bg: #e9e6e1;
    --card-bg: #f4f5f2;
    --brand-dark: #1f3a1c;
    --green-light: #5fb548;
    --green-mid: #3c8c34;
    --green-deep: #1c5a1f;
    --green-darkest: #0f4214;
    --divider: #cfe8c4;
    --text-light: #f3f8ef;
    --text-soft: #d8ebd0;
    --text-contact: #d9e4d6;
  }
  * { margin: 0; padding: 0; box-sizing: border-box; }
  html, body {
    width: 1200px; height: 969px; overflow: hidden;
    background: var(--page-bg);
    font-family: "Roboto", Arial, sans-serif;
  }
  .card {
    position: absolute; left: 100px; top: 202px;
    width: 1000px; height: 564px;
    background: var(--card-bg);
    box-shadow: 0 18px 40px rgba(0,0,0,0.18);
    overflow: hidden;
  }
  .card-bands { position: absolute; inset: 0; }
  .brand {
    position: absolute; top: 92px; left: 0; right: 0;
    display: flex; align-items: center; justify-content: center; gap: 22px;
  }
  .brand-mark { width: 46px; height: 46px; background: var(--green-mid); }
  .brand-name {
    font-weight: 700; font-size: 46px; letter-spacing: 1px;
    color: var(--brand-dark); text-transform: uppercase;
  }
  .person {
    position: absolute; right: 548px; top: 394px; text-align: right;
    color: var(--text-soft);
  }
  .person-name { font-weight: 500; font-size: 33px; color: var(--text-light); letter-spacing: 0.5px; }
  .person-title { font-size: 24px; margin-top: 2px; letter-spacing: 0.5px; }
  .person-address { font-size: 22px; line-height: 32px; margin-top: 2px; }
  .contacts {
    position: absolute; left: 560px; top: 400px; list-style: none;
    color: var(--text-contact); font-size: 22px;
  }
  .contact-item { display: flex; align-items: center; gap: 14px; height: 31px; }
  .contact-icon { width: 18px; height: 18px; fill: var(--green-light); flex: none; }
</style>
</head>
<body>
  <div class="card">
    <svg class="card-bands" viewBox="0 0 1000 564" preserveAspectRatio="none" aria-hidden="true">
      <defs>
        <linearGradient id="bandLeft" x1="0" y1="0" x2="1" y2="1">
          <stop offset="0" stop-color="var(--green-light)"/>
          <stop offset="1" stop-color="var(--green-mid)"/>
        </linearGradient>
        <linearGradient id="bandRight" x1="0" y1="0" x2="1" y2="1">
          <stop offset="0" stop-color="var(--green-deep)"/>
          <stop offset="1" stop-color="var(--green-darkest)"/>
        </linearGradient>
      </defs>
      <polygon points="0,384 500,288 500,564 0,564" fill="url(#bandLeft)"/>
      <polygon points="500,288 1000,360 1000,564 500,564" fill="url(#bandRight)"/>
      <line x1="500" y1="288" x2="500" y2="564" stroke="var(--divider)" stroke-width="2"/>
    </svg>

    <div class="brand">
      <span class="brand-mark"></span>
      <span class="brand-name">Brightline Retrofit Group</span>
    </div>

    <div class="person">
      <p class="person-name">DANIEL REYES</p>
      <p class="person-title">CEO/FOUNDER</p>
      <p class="person-address">1420 Harbor View Road<br>Juneau, Alaska 99801</p>
    </div>

    <ul class="contacts">
      <li class="contact-item">
        <svg class="contact-icon" viewBox="0 0 24 24"><path d="M6.6 10.8a15.1 15.1 0 0 0 6.6 6.6l2.2-2.2a1 1 0 0 1 1-.25 11.4 11.4 0 0 0 3.6.57 1 1 0 0 1 1 1V20a1 1 0 0 1-1 1A17 17 0 0 1 3 4a1 1 0 0 1 1-1h3.5a1 1 0 0 1 1 1c0 1.25.2 2.45.57 3.57a1 1 0 0 1-.25 1z"/></svg>
        <span>555 201 4730</span>
      </li>
      <li class="contact-item">
        <svg class="contact-icon" viewBox="0 0 24 24"><path d="M7 1h10a2 2 0 0 1 2 2v18a2 2 0 0 1-2 2H7a2 2 0 0 1-2-2V3a2 2 0 0 1 2-2zm0 3v14h10V4zm5 15.5a1 1 0 1 0 0 2 1 1 0 0 0 0-2z"/></svg>
        <span>555 318 6642</span>
      </li>
      <li class="contact-item">
        <svg class="contact-icon" viewBox="0 0 24 24"><path d="M6 2h9l3 3v4H6zm-2 8h16a2 2 0 0 1 2 2v6h-4v4H6v-4H2v-6a2 2 0 0 1 2-2zm4 6v4h8v-4z"/></svg>
        <span>555 774 1095</span>
      </li>
      <li class="contact-item">
        <svg class="contact-icon" viewBox="0 0 24 24"><path d="M2 5h20v14H2zm2 2v.4l8 5.2 8-5.2V7zm0 2.8V17h16V9.8l-8 5.2z"/></svg>
        <span>daniel@mailsite.com</span>
      </li>
    </ul>
  </div>
</body>
</html>
```